Veldon Tracing, Inc. - Stationary Project
Business Cards and Stationary for Missing Person Consultants
Professional
Luke Hammond
Search Coordinator
718 West Marlow Avenue
Suite #263
Orlando, FL 32806
lhammond@veldontracing-demo.org
www.VeldonTracing-demo.org
Our organization is called upon
when someone disappears. We¹d like to have a professional business card that
is very eye-catching and people will notice. Please use the red, black and
gray colors in the logo to make a great looking business card, letterhead
and envelope. We look forward to seeing your designs.
We'd like to see a clever use of the logo on the back of the card in bigger format.
This is our logo in AI format.

```html
<!DOCTYPE html>
<html lang="en">
<head>
<meta charset="utf-8">
<title>Veldon Tracing business cards</title>
<link href="https://fonts.googleapis.com/css2?family=Arimo:wght@400;700&display=swap" rel="stylesheet">
<style>
  :root {
    --backdrop: #5d5e60;
    --red: #c3161c;
    --red-dark: #7e0c10;
    --black: #111111;
    --charcoal: #2b2b2b;
    --gray: #6d6e70;
    --white: #ffffff;
  }
  html, body { margin: 0; padding: 0; overflow: hidden; }
  body {
    width: 1200px; height: 766px;
    background: var(--backdrop);
    font-family: "Arimo", Arial, sans-serif;
    position: relative;
  }
  .card {
    position: absolute;
    border-radius: 10px;
    overflow: hidden;
    box-shadow: 0 3px 10px rgba(0,0,0,.45);
  }
  .card--front { width: 436px; height: 220px; left: 156px; }
  .card--back { width: 446px; height: 220px; left: 606px; }
  .row-top { top: 172px; }
  .row-bottom { top: 444px; }
  .card--light { background: var(--white); }
  .card--dark { background: var(--black); }

  .band { position: absolute; left: 0; top: 0; width: 100%; height: 100%; }

  .holder { position: absolute; right: 22px; top: 12px; text-align: right; color: var(--white); }
  .holder__name { font-weight: 700; font-size: 17px; line-height: 20px; }
  .holder__title { font-size: 10px; line-height: 13px; }

  .brand {
    position: absolute;
    display: flex; align-items: center; gap: 8px;
    font-weight: 700; white-space: nowrap;
  }
  .brand__dot { border-radius: 50%; background: var(--red); flex: none; }
  .brand--front { left: 22px; top: 108px; font-size: 20px; color: var(--charcoal); }
  .brand--front .brand__dot { width: 26px; height: 26px; }
  .card--dark .brand--front { color: var(--white); }
  .brand--back { left: 50%; top: 70px; transform: translateX(-50%); font-size: 32px; color: var(--charcoal); }
  .brand--back .brand__dot { width: 48px; height: 48px; }
  .card--dark .brand--back { color: var(--white); }

  .contact {
    position: absolute; right: 22px; top: 142px;
    text-align: right; font-size: 7.5px; line-height: 11px; color: var(--charcoal);
  }
  .card--dark .contact { color: var(--white); }

  .back-web {
    position: absolute; left: 0; right: 0; bottom: 18px;
    text-align: center; font-size: 12px; color: var(--black);
  }
  .card--dark .back-web { color: var(--white); }
</style>
</head>
<body>

  <section class="card card--front card--light row-top">
    <svg class="band" viewBox="0 0 436 220" aria-hidden="true">
      <defs>
        <linearGradient id="redFade" x1="0" y1="0" x2="0" y2="1">
          <stop offset="0" stop-color="#e0262c"/>
          <stop offset="1" stop-color="#7e0c10"/>
        </linearGradient>
      </defs>
      <path d="M0 0H436V70C300 64 180 72 0 84Z" fill="url(#redFade)"/>
      <path d="M0 88C180 76 300 68 436 74" stroke="#2b2b2b" stroke-width="3" fill="none"/>
    </svg>
    <div class="holder">
      <div class="holder__name">Luke Hammond</div>
      <div class="holder__title">Search Coordinator</div>
    </div>
    <div class="brand brand--front"><span class="brand__dot"></span>Veldon Tracing</div>
    <div class="contact">
      718 West Marlow Avenue<br>
      Suite #263<br>
      Orlando, FL 32806<br>
      Cell: (507) 555-0148 &nbsp;|&nbsp; Fax: (520) 555-0193<br>
      Email: lhammond@veldontracing-demo.org &nbsp;|&nbsp; Web: www.VeldonTracing-demo.org
    </div>
  </section>

  <section class="card card--back card--light row-top">
    <div class="brand brand--back"><span class="brand__dot"></span>Veldon Tracing</div>
    <div class="back-web">www.VeldonTracing-demo.org</div>
  </section>

  <section class="card card--front card--dark row-bottom">
    <svg class="band" viewBox="0 0 436 220" aria-hidden="true">
      <defs>
        <linearGradient id="redFadeDark" x1="0" y1="0" x2="0" y2="1">
          <stop offset="0" stop-color="#e0262c"/>
          <stop offset="1" stop-color="#7e0c10"/>
        </linearGradient>
      </defs>
      <path d="M0 0H436V70C300 64 180 72 0 84Z" fill="url(#redFadeDark)"/>
      <path d="M0 84C180 72 300 64 436 70V80C300 74 180 84 0 96Z" fill="#ffffff"/>
    </svg>
    <div class="holder">
      <div class="holder__name">Luke Hammond</div>
      <div class="holder__title">Search Coordinator</div>
    </div>
    <div class="brand brand--front"><span class="brand__dot"></span>Veldon Tracing</div>
    <div class="contact">
      718 West Marlow Avenue<br>
      Suite #263<br>
      Orlando, FL 32806<br>
      Cell: (507) 555-0148 &nbsp;|&nbsp; Fax: (520) 555-0193<br>
      Email: lhammond@veldontracing-demo.org &nbsp;|&nbsp; Web: www.VeldonTracing-demo.org
    </div>
  </section>

  <section class="card card--back card--dark row-bottom">
    <div class="brand brand--back"><span class="brand__dot"></span>Veldon Tracing</div>
    <div class="back-web">www.VeldonTracing-demo.org</div>
  </section>

</body>
</html>
```